Australian Wine export company Need a Wine label design

We need a wine label design for a new branded Australian wine based in South Australia called " KESTRELMOOR " .
We will use this brand name ' KESTRELMOOR' to marketing Australian Red wine and White wine into Chinese Market.
We would like to see the label designs that look classic and make consumers feel this is a superior quality Australian wine.
This label is to promote AUSTRALIAN WINE, need wine related and country related theme, need to give the consumer first impression that this wine is from AUSTRALIA.

Thanks

The following information are required to be presented on the wine label:

1) Brand Name: Kestrelmoor
2) Logo
3) Year of Vintage
4) Varietal
5) Place of production: South Australia
6) Fine Wine of Australia

Thanks.

Target Market(s)

Chinese market

Industry/Entity Type

Marketing

Requirements
Must have
• Need label design and renderings on the bottles.
Nice to have
• Label make consumers feel this is a superior quality Australian Wine.

```html
<!DOCTYPE html>
<html lang="en">
<head>
<meta charset="utf-8">
<title>Kestrelmoor Wine Label Variations</title>
<link href="https://fonts.googleapis.com/css2?family=Tinos:wght@400;700&family=Questrial&display=swap" rel="stylesheet">
<style>
  :root {
    --canvas: #ffffff;
    --label-paper: #f2f2ef;
    --ink: #2a2a2a;
    --gold: #b3a82a;
    --gold-deep: #9c9220;
    --band-text: #fbf8e6;
  }
  * { margin: 0; padding: 0; box-sizing: border-box; }
  html, body {
    width: 1200px; height: 900px; overflow: hidden;
    background: var(--canvas);
  }
  .label-set { position: relative; width: 1200px; height: 900px; }
  .label {
    position: absolute; top: 390px;
    width: 213px; height: 258px;
    background: var(--label-paper);
    box-shadow: 0 1px 3px rgba(0,0,0,0.12);
    color: var(--ink);
    text-align: center;
    font-family: "Tinos", "Times New Roman", serif;
  }
  .label--classic { left: 105px; }
  .label--script  { left: 365px; }
  .label--wide    { left: 625px; }
  .label--modern  { left: 888px; }

  .brand-mark {
    position: absolute; top: 40px; left: 50%;
    width: 20px; height: 20px; margin-left: -10px;
    border-radius: 50%;
    background: var(--gold);
  }
  .brand-name {
    position: absolute; top: 78px; left: 0; right: 0;
    font-weight: 400; line-height: 1;
  }
  .label--classic .brand-name { font-size: 13px; letter-spacing: 0.22em; }
  .label--script .brand-name { top: 76px; font-size: 23px; letter-spacing: 0.06em; }
  .label--wide .brand-name { font-size: 15px; letter-spacing: 0.2em; }
  .label--modern .brand-name {
    top: 86px;
    font-family: "Questrial", "Helvetica", sans-serif;
    font-size: 14px; letter-spacing: 0.14em;
  }

  .details {
    position: absolute; top: 126px; left: 0; right: 0;
    font-size: 11px; line-height: 19px; letter-spacing: 0.04em;
  }
  .label--script .details { top: 128px; font-weight: 700; line-height: 20px; }
  .label--modern .details {
    top: 130px;
    font-family: "Questrial", "Helvetica", sans-serif;
    font-size: 10px; line-height: 18px;
  }

  .origin-band {
    position: absolute; top: 228px; left: 0; right: 0; height: 28px;
    background: linear-gradient(to bottom, var(--gold), var(--gold-deep));
    color: var(--band-text);
    font-size: 7.5px; font-weight: 700; letter-spacing: 0.1em;
    line-height: 28px;
  }
  .label--modern .origin-band { font-family: "Questrial", "Helvetica", sans-serif; }
</style>
</head>
<body>
  <main class="label-set">
    <section class="label label--classic">
      <span class="brand-mark" aria-hidden="true"></span>
      <h1 class="brand-name">KESTRELMOOR</h1>
      <p class="details">South Australia<br>Cabernet Sauvignon<br>2012</p>
      <p class="origin-band">FINE WINE OF AUSTRALIA</p>
    </section>

    <section class="label label--script">
      <span class="brand-mark" aria-hidden="true"></span>
      <h1 class="brand-name">Kestrelmoor</h1>
      <p class="details">South Australia<br>Cabernet Sauvignon<br>2012</p>
      <p class="origin-band">FINE WINE OF AUSTRALIA</p>
    </section>

    <section class="label label--wide">
      <span class="brand-mark" aria-hidden="true"></span>
      <h1 class="brand-name">KESTRELMOOR</h1>
      <p class="details">South Australia<br>Cabernet Sauvignon<br>2012</p>
      <p class="origin-band">FINE WINE OF AUSTRALIA</p>
    </section>

    <section class="label label--modern">
      <span class="brand-mark" aria-hidden="true"></span>
      <h1 class="brand-name">KESTRELMOOR</h1>
      <p class="details">South Australia<br>Cabernet Sauvignon<br>2012</p>
      <p class="origin-band">FINE WINE OF AUSTRALIA</p>
    </section>
  </main>
</body>
</html>
```